Business Card Design For Financial Company

Create a new design for company's business card. The corporate logo is attached in several formats. Our new website design is also attached and we would like the business cards to reflect this.
Card needs to contain the following info:
Name
Job Title
Legal company name - eg Volmar Capital (Asia) Ltd
Address - eg 612-15 Dorrance Plaza,47 Faverly Street, Hong Kong
Direct tel
Main tel
Fax
Email
Website URL
MS word format preferred. Other formats that can be edited on standard PC also OK.
Please note the the "VOLMAR" logo nameĀ font is "Gill Sans MT" on Windows
Target Market(s)
Instituation Investors
Industry/Entity Type
Business

```html
<!DOCTYPE html>
<html lang="en">
<head>
<meta charset="utf-8">
<title>Volmar Capital – Business Card</title>
<link rel="stylesheet" href="https://fonts.googleapis.com/css2?family=Lato:wght@400&family=Roboto+Condensed:wght@300&family=Source+Sans+3:wght@400;600&display=swap">
<style>
  :root {
    --backdrop: #ece9e4;
    --card: #ffffff;
    --ink: #1c1c1c;
    --muted: #6b6b6b;
    --accent: #6e1a22;
    --rule: #d4d4d4;
  }
  * { margin: 0; padding: 0; box-sizing: border-box; }
  html, body { width: 1200px; height: 449px; overflow: hidden; }
  body {
    background: var(--backdrop);
    position: relative;
    font-family: "Source Sans 3", "Helvetica Neue", Arial, sans-serif;
    color: var(--muted);
  }
  .card {
    position: absolute;
    background: var(--card);
    width: 538px;
    height: 307px;
    box-shadow: 0 2px 6px rgba(0,0,0,0.18);
  }
  .card--front { left: 43px; top: 72px; }
  .card--back { left: 618px; top: 70px; }

  .lockup {
    position: absolute;
    display: flex;
    align-items: center;
    gap: 12px;
  }
  .brand-square {
    width: 14px;
    height: 14px;
    background: var(--accent);
  }
  .brand-name {
    font-family: "Lato", "Gill Sans", sans-serif;
    font-weight: 400;
    font-size: 32px;
    letter-spacing: 1px;
    color: var(--ink);
    line-height: 1;
  }
  .tagline {
    position: absolute;
    font-family: "Roboto Condensed", "Arial Narrow", sans-serif;
    font-weight: 300;
    text-transform: uppercase;
    color: var(--muted);
    white-space: nowrap;
  }

  /* front */
  .card--front .lockup { left: 52px; top: 108px; }
  .card--front .tagline { left: 46px; top: 174px; font-size: 10.5px; }
  .address {
    position: absolute;
    left: 57px; top: 216px;
    font-size: 12px;
    line-height: 20px;
    font-style: normal;
  }
  .divider {
    position: absolute;
    left: 301px; top: 76px;
    width: 1px; height: 178px;
    background: var(--rule);
  }
  .contact {
    position: absolute;
    left: 318px; top: 76px;
    font-size: 11.5px;
  }
  .contact__name { font-size: 15px; font-weight: 600; color: var(--accent); line-height: 18px; }
  .contact__title { font-size: 11.5px; color: var(--muted); line-height: 16px; margin-bottom: 14px; }
  .contact__list { list-style: none; }
  .contact__list li { line-height: 19.4px; white-space: nowrap; }
  .contact__label { color: var(--accent); }
  .contact__web { margin-top: 11px; font-size: 13px; font-weight: 600; color: var(--accent); }

  /* back */
  .card--back .lockup { left: 0; right: 0; top: 122px; justify-content: center; }
  .card--back .tagline {
    left: 0; right: 0; top: 225px;
    text-align: center;
    font-size: 12px;
    letter-spacing: 2px;
  }
</style>
</head>
<body>
  <section class="card card--front" aria-label="Business card front">
    <div class="lockup">
      <span class="brand-square" aria-hidden="true"></span>
      <span class="brand-name">VOLMAR</span>
    </div>
    <p class="tagline">Institutional Research Advisory and Trading</p>
    <address class="address">612-15 Dorrance Plaza<br>47 Faverly Street, Hong Kong</address>
    <span class="divider" aria-hidden="true"></span>
    <div class="contact">
      <p class="contact__name">Eliot Marsh</p>
      <p class="contact__title">Head of Reasearch</p>
      <ul class="contact__list">
        <li><span class="contact__label">Direct</span> - +852 3987 2140</li>
        <li><span class="contact__label">Mobile</span> - +852 3987 2140</li>
        <li><span class="contact__label">Desk</span> - +852 3987 2140 (optional)</li>
        <li><span class="contact__label">Fax</span> - +852 3987 2140</li>
        <li><span class="contact__label">Email</span> - eliot.marsh@volmarcapital.com</li>
      </ul>
      <p class="contact__web">www.volmarcapital.com</p>
    </div>
  </section>

  <section class="card card--back" aria-label="Business card back">
    <div class="lockup">
      <span class="brand-square" aria-hidden="true"></span>
      <span class="brand-name">VOLMAR</span>
    </div>
    <p class="tagline">Institutional Research Advisory and Trading</p>
  </section>
</body>
</html>
```